Professional Single Page Website Design for Vellowind Advisory

Vellowind Advisory is a new business consultancy specializing in providing expert services to small businesses, primarily in the brick-and-mortar retail and food service sectors. We offer a range of services including franchise development and launch, due diligence, and construction management.

Currently, we have a basic website set up at www.vellowindadvisory.example, but we need a professional touch to enhance its design and functionality.

Project Requirements:
- Single Page Design: For now, we need a single page design that effectively showcases who we are, our services, and contact information.
- Future Expansion: The design should be flexible and scalable for future expansion to include additional pages like specific service offerings, about us, and a dedicated contact page.
- Design Aesthetic: We are looking for a modern yet professional design that aligns with our brand identity.
- Logo: We have a logo that we like, which was also sourced from Pixel Forum. The logo files are attached to this project brief.

Key Sections to Include:
- Hero Section: An engaging introduction to Vellowind Advisory with a strong visual impact.
- About Us: A brief overview of who we are and our mission.
- Team: Section for the profiles of the two principals.
- Services: A clear and concise presentation of our services, including franchise development, due diligence, and construction management.
- Contact Information: Easy-to-find contact details, including a form for inquiries.
- Call to Action: Encouraging visitors to get in touch with us for consultations or further information.

Design Considerations:
- Ensure the design is responsive and mobile-friendly.
- Include high-quality images and icons that complement our services and industry.
- We do not need development services, this is only a design project.

```html
<!DOCTYPE html>
<html lang="en">
<head>
<meta charset="utf-8">
<title>Vellowind Advisory</title>
<link rel="stylesheet" href="https://fonts.googleapis.com/css2?family=Poppins:wght@400;500;600&display=swap">
<style>
:root{
  --mint:#94c7b1;
  --mint-soft:#e4f1eb;
  --ink:#1f2933;
  --navy:#1e2833;
  --text:#3a4149;
  --muted:#5c636a;
  --line:#d9dde0;
  --white:#ffffff;
}
*{box-sizing:border-box;margin:0;padding:0}
html,body{width:1200px;height:3676px;overflow:hidden}
body{font-family:'Poppins',sans-serif;color:var(--ink);background:var(--white);position:relative}
.abs{position:absolute}
.brand{display:flex;align-items:center;gap:10px;font-weight:600;color:var(--ink)}
.brand-dot{width:22px;height:22px;border-radius:50%;background:var(--ink)}
.brand-name{font-size:20px;line-height:1}

/* header */
.site-header{position:absolute;left:0;top:0;width:1200px;height:110px}
.site-header .brand{position:absolute;left:111px;top:42px}
.main-nav{position:absolute;left:514px;top:46px;display:flex;gap:25px;font-size:15px;color:var(--text)}
.main-nav a{color:inherit;text-decoration:none}
.main-nav a.active{color:var(--mint);font-weight:500}
.btn{display:inline-flex;align-items:center;justify-content:center;font-family:inherit;font-weight:500;font-size:15px;border:0;border-radius:4px;text-decoration:none}
.btn-mint{background:var(--mint);color:var(--ink)}
.btn-dark{background:var(--navy);color:var(--white)}
.header-cta{position:absolute;left:949px;top:34px;width:140px;height:43px}

/* hero */
.hero-shape{position:absolute;left:560px;top:185px;width:190px;height:190px;border-radius:46px;background:var(--mint-soft);transform:rotate(45deg)}
.hero-photo{position:absolute;left:710px;top:142px;width:350px;height:350px;border-radius:80px;transform:rotate(45deg);background:linear-gradient(135deg,#5b7fa8,#2d4f7a 55%,#1b2f4d)}
.hero-title{position:absolute;left:111px;top:168px;font-size:49px;font-weight:600;line-height:58px;color:var(--ink);width:600px}
.hero-sub{position:absolute;left:113px;top:303px;font-size:17px}
.hero-sub strong{font-weight:600}
.hero-text{position:absolute;left:113px;top:344px;width:460px;font-size:17px;line-height:30px;color:var(--text)}
.hero-cta{position:absolute;left:113px;top:462px;width:191px;height:42px;font-size:15px}

/* about */
.about{position:absolute;left:0;top:592px;width:1200px;height:614px;background:var(--navy);overflow:hidden}
.about-photo{position:absolute;left:0;top:0;width:860px;height:614px;background:linear-gradient(100deg,#8a6a4c 0%,#5a6878 30%,#3d4b5a 60%,rgba(30,40,51,0) 100%)}
.about-body{position:absolute;left:565px;top:80px;width:524px;color:var(--white)}
.about-body h2{font-size:47px;font-weight:600;color:var(--mint);line-height:60px;margin-bottom:20px}
.about-body p{font-size:15px;line-height:28.3px;text-align:justify;margin-bottom:14px}

/* services */
.section-title{position:absolute;left:0;width:1200px;text-align:center;font-size:47px;font-weight:600;color:var(--mint)}
.service-card{position:absolute;top:1396px;width:306px;height:302px;text-align:center}
.service-card.active{background:var(--white);box-shadow:0 4px 18px rgba(0,0,0,.08);z-index:2}
.service-card svg{position:absolute;left:93px;top:61px}
.service-card h3{position:absolute;left:0;top:200px;width:100%;font-size:17px;font-weight:500;line-height:28px;letter-spacing:.3px}
.arrow{position:absolute;top:1563px}
.service-panel{position:absolute;left:111px;top:1684px;width:976px;height:585px;background:var(--mint);border-radius:4px}
.service-panel h3{position:absolute;left:43px;top:47px;font-size:36px;font-weight:600;line-height:47px;color:var(--white)}
.service-panel .copy{position:absolute;left:43px;top:153px;width:457px;color:var(--white);font-size:14.5px;line-height:27.5px;text-align:justify}
.service-panel .copy p{margin-bottom:15px}
.service-art{position:absolute;left:531px;top:150px;width:420px;height:300px;border-radius:6px;background:radial-gradient(circle at 50% 45%,#c7ddd3,#a8d0bf 70%)}

/* team */
.team-card{position:absolute;top:2459px;width:474px;height:320px;background:var(--white);box-shadow:0 4px 18px rgba(0,0,0,.07);overflow:hidden}
.team-card .corner{position:absolute;right:-50px;top:-50px;width:150px;height:150px;border-radius:50%;background:var(--navy);box-shadow:0 0 0 14px var(--mint)}
.team-card .corner svg{position:absolute;left:36px;top:64px}
.avatar{position:absolute;left:32px;top:34px;width:120px;height:120px;border-radius:50%;border:3px solid var(--mint);background:linear-gradient(160deg,#b4a89b,#6d6259)}
.team-card h3{position:absolute;left:173px;top:62px;font-size:22px;font-weight:500}
.team-card .role{position:absolute;left:173px;top:96px;font-size:16px;font-weight:500}
.team-card .bio{position:absolute;left:34px;top:176px;width:420px;font-size:14.5px;line-height:28px;color:var(--text)}

/* contact */
.contact-info{position:absolute;left:114px;top:3030px}
.contact-info h3{font-size:24px;font-weight:500;margin-bottom:28px}
.info-item{position:relative;padding-left:32px;margin-bottom:24px;font-size:17px;line-height:26px}
.info-item b{font-weight:500;display:block}
.info-item svg{position:absolute;left:0;top:3px}
.contact-form{position:absolute;left:599px;top:2994px;width:491px;height:434px;background:var(--white);box-shadow:0 4px 18px rgba(0,0,0,.08)}
.contact-form h3{position:absolute;left:38px;top:48px;font-size:24px;font-weight:500}
.field{position:absolute;left:37px;width:411px;border:1px solid var(--line);border-radius:2px;font-family:inherit;font-size:15px;color:#8a9096;padding:12px 20px}
.contact-form .btn{position:absolute;left:37px;top:357px;width:140px;height:43px}

/* footer */
.site-footer{position:absolute;left:0;top:3488px;width:1200px;height:188px;background:var(--navy);color:var(--white)}
.site-footer .brand{position:absolute;left:111px;top:86px;color:var(--white)}
.site-footer .brand-dot{background:var(--white)}
.site-footer .brand-name{font-size:26px}
.footer-nav{position:absolute;right:111px;top:60px;display:flex;gap:26px;font-size:15px}
.footer-nav a{color:inherit;text-decoration:none}
.copyright{position:absolute;right:111px;top:103px;font-size:15px}
</style>
</head>
<body>

<header class="site-header">
  <div class="brand"><span class="brand-dot"></span><span class="brand-name">Vellowind Advisory</span></div>
  <nav class="main-nav">
    <a class="active" href="#">Home</a><a href="#">About Us</a><a href="#">Team</a><a href="#">Services</a><a href="#">Contact Us</a>
  </nav>
  <a class="btn btn-mint header-cta" href="#">Get in Touch</a>
</header>

<section class="hero">
  <div class="hero-shape"></div>
  <div class="hero-photo" role="img" aria-label="Photo of a smiling businessman in a blue suit by a city building"></div>
  <h1 class="hero-title">Building Success in Southern California</h1>
  <p class="hero-sub"><strong>Expertise at Every Step</strong>: From Planning to Execution</p>
  <p class="hero-text">At Vellowind, we blend innovative strategies with local market expertise to guide your commercial real estate ventures.</p>
  <a class="btn btn-dark hero-cta" href="#">Book consultations</a>
</section>

<section class="about">
  <div class="about-photo" role="img" aria-label="Photo looking up at downtown skyscrapers and a historic brick building"></div>
  <div class="about-body">
    <h2>About Us</h2>
    <p>Welcome to Vellowind Advisory, your trusted partner in navigating the complexities of the real estate and small business markets. Founded by industry veterans Ethan Morrow and Daniel Okafor, we specialize in providing comprehensive services tailored to the unique needs of our clients. Whether you're a franchisee, a new restaurant owner, or a commercial real estate investor, our expertise in due diligence, construction management, and investment property evaluation ensures you make informed, strategic decisions.</p>
    <p>At Vellowind Advisory, we are committed to your success. Our approach combines meticulous analysis, strategic insights, and personalized service to help you achieve your business goals. We pride ourselves on our ability to deliver results that exceed expectations, fostering long-term relationships built on trust and excellence.</p>
  </div>
</section>

<h2 class="section-title" style="top:1268px">Our Services</h2>

<svg class="arrow" style="left:46px" width="20" height="26" viewBox="0 0 20 26"><path d="M14 3 4 13l10 10" fill="none" stroke="#1f2933" stroke-width="3"/></svg>
<svg class="arrow" style="left:1136px" width="20" height="26" viewBox="0 0 20 26"><path d="M6 3l10 10-10 10" fill="none" stroke="#1f2933" stroke-width="3"/></svg>

<div class="service-card active" style="left:114px">
  <svg width="120" height="120" viewBox="0 0 120 120"><circle cx="60" cy="60" r="58" fill="none" stroke="#4f6b63" stroke-width="3"/><rect x="32" y="34" width="52" height="40" rx="4" fill="none" stroke="#4f6b63" stroke-width="2.5"/><path d="M32 44h52M47 55l-5 4 5 4M57 55l5 4-5 4" fill="none" stroke="#4f6b63" stroke-width="2.5"/><circle cx="78" cy="72" r="10" fill="#fff" stroke="#4f6b63" stroke-width="2.5"/><circle cx="78" cy="72" r="3.5" fill="none" stroke="#4f6b63" stroke-width="2"/></svg>
  <h3>FRANCHISE DEVELOPMENT<br>&amp; LAUNCH</h3>
</div>
<div class="service-card" style="left:446px">
  <svg width="120" height="120" viewBox="0 0 120 120"><circle cx="60" cy="60" r="58" fill="none" stroke="#4f6b63" stroke-width="3"/><rect x="32" y="34" width="52" height="40" rx="4" fill="none" stroke="#4f6b63" stroke-width="2.5"/><path d="M32 44h52M47 55l-5 4 5 4M57 55l5 4-5 4" fill="none" stroke="#4f6b63" stroke-width="2.5"/><circle cx="78" cy="72" r="10" fill="#fff" stroke="#4f6b63" stroke-width="2.5"/><circle cx="78" cy="72" r="3.5" fill="none" stroke="#4f6b63" stroke-width="2"/></svg>
  <h3>BUILDING &amp; CONSTRUCTION<br>MANAGEMENT</h3>
</div>
<div class="service-card" style="left:778px">
  <svg width="120" height="120" viewBox="0 0 120 120"><circle cx="60" cy="60" r="58" fill="none" stroke="#4f6b63" stroke-width="3"/><rect x="32" y="34" width="52" height="40" rx="4" fill="none" stroke="#4f6b63" stroke-width="2.5"/><path d="M32 44h52M47 55l-5 4 5 4M57 55l5 4-5 4" fill="none" stroke="#4f6b63" stroke-width="2.5"/><circle cx="78" cy="72" r="10" fill="#fff" stroke="#4f6b63" stroke-width="2.5"/><circle cx="78" cy="72" r="3.5" fill="none" stroke="#4f6b63" stroke-width="2"/></svg>
  <h3>INVESTMENT PROPERTY<br>EVALUATION</h3>
</div>

<div class="service-panel">
  <h3>Franchise<br>Development &amp; Launch</h3>
  <div class="copy">
    <p>At Vellowind Advisory, our Franchise Development &amp; Launch service is designed to transform your successful business into a thriving franchise. We start by thoroughly evaluating your business model to determine its franchisability. Once confirmed, our team handles every aspect of the franchise setup, including legal documentation, branding, marketing strategies, operational guidelines, and franchisee recruitment.</p>
    <p>Our goal is to ensure a seamless and efficient transition from a single successful location to a robust franchise network, empowering your business to scale effectively and achieve exponential growth. Partner with us to turn your business into a nationwide brand.</p>
  </div>
  <div class="service-art" role="img" aria-label="Illustration of a central franchise store with arrows branching out to many smaller stores"></div>
</div>

<h2 class="section-title" style="top:2330px">Our Leadership Team</h2>

<article class="team-card" style="left:114px">
  <div class="corner"><svg width="34" height="30" viewBox="0 0 34 30"><path d="M6 4c2 0 4 4 4 6s-3 2-2 4 5 6 7 7 2-2 4-2 6 2 6 4-3 4-6 4C14 27 3 16 3 8c0-2 1-4 3-4z" fill="#fff"/></svg></div>
  <div class="avatar" role="img" aria-label="Portrait photo of Daniel Okafor"></div>
  <h3>DANIEL OKAFOR</h3>
  <p class="role">PRINCIPAL</p>
  <p class="bio">Daniel Okafor is a seasoned real estate expert with extensive experience in project and construction management, and a licensed real estate agent in California. Fluent in both English and Korean,</p>
</article>
<article class="team-card" style="left:615px">
  <div class="corner"><svg width="34" height="30" viewBox="0 0 34 30"><path d="M6 4c2 0 4 4 4 6s-3 2-2 4 5 6 7 7 2-2 4-2 6 2 6 4-3 4-6 4C14 27 3 16 3 8c0-2 1-4 3-4z" fill="#fff"/></svg></div>
  <div class="avatar" role="img" aria-label="Portrait photo of Ethan Morrow" style="background:linear-gradient(160deg,#9cb6cf,#e8eef3)"></div>
  <h3>ETHAN MORROW</h3>
  <p class="role">PRINCIPAL</p>
  <p class="bio">Ethan Morrow brings almost 20 years of rich experience as a real estate investor and a pivotal role at one of southern California's largest real estate management firms, where he</p>
</article>

<h2 class="section-title" style="top:2875px">Contact Us</h2>

<div class="contact-info">
  <h3>Contact Information</h3>
  <div class="info-item"><svg width="20" height="24" viewBox="0 0 20 24"><path d="M10 1a8 8 0 0 0-8 8c0 6 8 14 8 14s8-8 8-14a8 8 0 0 0-8-8z" fill="#1a5fa0"/><circle cx="10" cy="9" r="3" fill="#fff"/></svg><b>Address:</b>214 Harbor Ridge Ave Suite 300<br>CA 90210</div>
  <div class="info-item"><svg width="20" height="20" viewBox="0 0 34 30"><path d="M6 4c2 0 4 4 4 6s-3 2-2 4 5 6 7 7 2-2 4-2 6 2 6 4-3 4-6 4C14 27 3 16 3 8c0-2 1-4 3-4z" fill="#1a5fa0"/></svg><b>Main Number:</b>+1800-555-0142</div>
  <div class="info-item"><svg width="20" height="16" viewBox="0 0 20 16"><rect x="1" y="1" width="18" height="14" rx="1" fill="#1a5fa0"/><path d="M1 2l9 7 9-7" fill="none" stroke="#fff" stroke-width="1.5"/></svg><b>Email:</b>info@vellowindadvisory.example</div>
</div>

<form class="contact-form">
  <h3>Fill the form</h3>
  <div class="field" style="top:95px;height:50px">Name</div>
  <div class="field" style="top:163px;height:50px">Email Address</div>
  <div class="field" style="top:231px;height:108px">Message</div>
  <span class="btn btn-mint">Get in Touch</span>
</form>

<footer class="site-footer">
  <div class="brand"><span class="brand-dot"></span><span class="brand-name">Vellowind Advisory</span></div>
  <nav class="footer-nav"><a href="#">Home</a><a href="#">About Us</a><a href="#">Team</a><a href="#">Services</a><a href="#">Contact Us</a></nav>
  <p class="copyright">2024 Vellowind Advisory. All Rights Reserved.</p>
</footer>

</body>
</html>
```